Salt, Silence and Sunrise Redesign

I am looking for a redesign on my book cover. I would like to keep the same title, subtitle and author name. This book is for women between the ages of 45 - 55 that are also dealing with health and hormone issues. So if there's a photo used of a woman, it should reflect that age group and a look of frustration or hopelessness. I would also like a notation that I am a best selling author and second edition. I have attached the current book cover and a copy of my business logo. Perhaps some consistency with my business logo would be a good idea and not necessary.
I have also attached an updated back cover with an edit in text and a new picture.
If it's helpful, I am a natural doctor known as a Traditional Naturopath and my primary focus of business is helping women overcome menopause symptoms.
Note, I do not want the use of any medical pictures, such as a stethoscope or a doctor in a white coat.
I am looking for different look and theme from my current cover. Something that is a bit more luxurious or upscale from my past cover.

```html
<!DOCTYPE html>
<html lang="en">
<head>
<meta charset="utf-8">
<title>Salt, Silence and Sunrise? — Second Edition Book Cover</title>
<link rel="stylesheet" href="https://fonts.googleapis.com/css2?family=Playfair+Display:wght@700&family=Cormorant+Garamond:ital,wght@0,500;1,500;1,600&family=Open+Sans:ital,wght@0,400;1,400&family=Montserrat:wght@600&display=swap">
<style>
  :root {
    --wine-deep: #2c111c;
    --wine: #4e1a2b;
    --wine-mid: #6d2639;
    --gold: #c49a5a;
    --gold-light: #e3c894;
    --cream: #f7efe6;
    --cream-deep: #ecdfd1;
    --ink: #2f2427;
    --isbn: #ffffff;
  }
  * { margin: 0; padding: 0; box-sizing: border-box; }
  html, body { width: 1200px; height: 877px; overflow: hidden; background: #fff; }
  .cover { position: relative; width: 1200px; height: 877px; overflow: hidden; font-family: "Open Sans", sans-serif; color: var(--ink); }

  .label {
    font-family: "Montserrat", sans-serif; font-weight: 600; text-transform: uppercase;
    letter-spacing: 4px; font-size: 12px; color: var(--gold);
  }

  /* Back cover */
  .back {
    position: absolute; left: 0; top: 0; width: 575px; height: 877px;
    background: linear-gradient(165deg, var(--cream) 0%, #f3e8de 60%, var(--cream-deep) 100%);
  }
  .back-title {
    position: absolute; left: 30px; top: 64px; width: 515px; text-align: center;
    font-family: "Playfair Display", serif; font-weight: 700; font-size: 25px; color: var(--wine);
    letter-spacing: 0.5px;
  }
  .back-subtitle {
    position: absolute; left: 30px; top: 104px; width: 515px; text-align: center;
    font-family: "Cormorant Garamond", serif; font-style: italic; font-weight: 500; font-size: 22px; color: var(--wine-mid);
  }
  .back-divider { position: absolute; left: 247px; top: 146px; width: 80px; height: 1px; background: var(--gold); }
  .back-blurb { position: absolute; left: 34px; top: 168px; width: 507px; font-size: 13.5px; line-height: 19px; }
  .back-blurb p + p { margin-top: 16px; }
  .back-tagline {
    position: absolute; left: 30px; top: 366px; width: 515px; text-align: center;
    font-family: "Cormorant Garamond", serif; font-style: italic; font-weight: 600; font-size: 27px; color: var(--wine);
  }
  .back-rule { position: absolute; left: 34px; top: 424px; width: 507px; height: 1px; background: var(--gold); }
  .author-photo {
    position: absolute; left: 34px; top: 456px; width: 188px; height: 226px;
    background: linear-gradient(160deg, #e4d3cb 0%, #c9aa9c 55%, #a98b86 100%);
    outline: 1px solid var(--gold); outline-offset: 5px;
  }
  .author-bio { position: absolute; left: 246px; top: 456px; width: 296px; font-size: 12px; line-height: 16.5px; font-style: italic; }
  .author-bio p + p { margin-top: 12px; }

  .back-band {
    position: absolute; left: 0; top: 709px; width: 575px; height: 168px;
    background: linear-gradient(135deg, var(--wine) 0%, var(--wine-deep) 100%);
    border-top: 2px solid var(--gold);
  }
  .brand { position: absolute; left: 34px; top: 66px; display: flex; align-items: center; gap: 10px; }
  .brand-dot { width: 22px; height: 22px; border-radius: 50%; background: var(--gold); }
  .brand-name { font-family: "Playfair Display", serif; font-weight: 700; font-size: 24px; color: var(--gold-light); }
  .isbn-box { position: absolute; left: 329px; top: 14px; width: 212px; height: 128px; background: var(--isbn); }

  /* Spine */
  .spine {
    position: absolute; left: 575px; top: 0; width: 50px; height: 877px;
    background: linear-gradient(90deg, var(--wine-deep) 0%, var(--wine) 50%, var(--wine-deep) 100%);
  }
  .spine-text {
    position: absolute; left: 50%; transform-origin: 0 0; white-space: nowrap;
    font-family: "Playfair Display", serif; font-weight: 700; color: var(--gold-light); font-size: 20px; letter-spacing: 1px;
  }
  .spine-title { top: 40px; transform: rotate(90deg) translateY(-50%); }
  .spine-author { top: 700px; transform: rotate(90deg) translateY(-50%); }

  /* Front cover */
  .front {
    position: absolute; left: 625px; top: 0; width: 575px; height: 877px;
    background: linear-gradient(180deg, var(--cream) 0%, #f3e7dc 100%);
  }
  .edition {
    position: absolute; left: 0; top: 26px; width: 575px;
    display: flex; align-items: center; justify-content: center; gap: 14px;
  }
  .edition-rule { width: 60px; height: 1px; background: var(--gold); }
  .front-title { position: absolute; left: 20px; top: 50px; width: 535px; height: 200px; }
  .front-subtitle {
    position: absolute; left: 0; top: 254px; width: 575px; text-align: center;
    font-family: "Cormorant Garamond", serif; font-style: italic; font-weight: 500; font-size: 25px; color: var(--wine-mid);
  }
  .cover-photo {
    position: absolute; left: 48px; top: 304px; width: 479px; height: 380px;
    background: linear-gradient(170deg, #e8dcd4 0%, #cfb3a4 45%, #9e7d72 100%);
    outline: 1px solid var(--gold); outline-offset: 6px;
  }
  .front-band {
    position: absolute; left: 0; top: 709px; width: 575px; height: 168px;
    background: linear-gradient(135deg, var(--wine) 0%, var(--wine-deep) 100%);
    border-top: 2px solid var(--gold); text-align: center;
  }
  .bestseller { margin-top: 20px; }
  .author-name {
    margin-top: 4px; font-family: "Playfair Display", serif; font-weight: 700; font-size: 50px;
    line-height: 60px; color: var(--cream); letter-spacing: 3px;
  }
  .author-role { font-family: "Cormorant Garamond", serif; font-weight: 500; font-size: 24px; line-height: 28px; color: var(--gold-light); letter-spacing: 1px; }
  .foreword { margin-top: 2px; font-family: "Cormorant Garamond", serif; font-style: italic; font-weight: 500; font-size: 18px; color: var(--cream); }
</style>
</head>
<body>
<div class="cover">

  <section class="back">
    <h2 class="back-title">SALT, SILENCE, AND SUNRISE?</h2>
    <p class="back-subtitle">How to Reverse the Clock and Feel Young Again</p>
    <div class="back-divider"></div>
    <div class="back-blurb">
      <p>Imagine how good it feels when you are able to easily slip into your sexy skinny jeans, have energy all day and feel truly happy. “Salt, Silence and Sunrise?” provides proven and effective secrets that give you the ability to achieve this all the while getting your life back on many levels.</p>
      <p>It’s a book that explains the how and why you became overweight, fatigued and frustrated in the first place. It outlines simple, effective, and proven strategies in a step by step way that will have you slipping on your skinny jeans, enjoying abundant energy and returning to your happy self again.</p>
    </div>
    <p class="back-tagline">Yes, you can reverse the clock!</p>
    <div class="back-rule"></div>
    <div class="author-photo" role="img" aria-label="Portrait photo of the author smiling, in a light shirt"></div>
    <div class="author-bio">
      <p>Traditional Naturopath, Arlen Voss was able to overcome epilepsy naturally and in the process a passion erupted inside of him to help people heal “incurable” health diseases. Since then Arlen has stayed at the forefront of Natural Medicine by working alongside leaders in the field, most notably Dr. Miles Harrow.</p>
      <p>This book is a result of his research, experience, and the learnings from helping thousands of people, just like you, overcome varying health challenges.</p>
    </div>
    <div class="back-band">
      <div class="brand">
        <span class="brand-dot"></span>
        <span class="brand-name">Voss Wellness</span>
      </div>
      <div class="isbn-box"></div>
    </div>
  </section>

  <section class="spine">
    <span class="spine-text spine-title">SALT, SILENCE, AND SUNRISE?</span>
    <span class="spine-text spine-author">ARLEN VOSS</span>
  </section>

  <section class="front">
    <div class="edition">
      <span class="edition-rule"></span>
      <span class="label">Second Edition</span>
      <span class="edition-rule"></span>
    </div>
    <svg class="front-title" viewBox="0 0 535 200" aria-label="Salt, Silence, and Sunrise?">
      <defs>
        <linearGradient id="titleFill" x1="0" y1="0" x2="1" y2="0">
          <stop offset="0" stop-color="#4e1a2b"/>
          <stop offset="0.5" stop-color="#7a2c3f"/>
          <stop offset="1" stop-color="#4e1a2b"/>
        </linearGradient>
      </defs>
      <text x="267" y="64" text-anchor="middle" font-family="'Playfair Display', serif" font-weight="700" font-size="58" fill="url(#titleFill)" textLength="500" lengthAdjust="spacingAndGlyphs">SALT, SILENCE,</text>
      <rect x="70" y="103" width="150" height="1" fill="#c49a5a"/>
      <rect x="315" y="103" width="150" height="1" fill="#c49a5a"/>
      <text x="267" y="113" text-anchor="middle" font-family="'Cormorant Garamond', serif" font-style="italic" font-weight="600" font-size="32" fill="#c49a5a">and</text>
      <text x="267" y="186" text-anchor="middle" font-family="'Playfair Display', serif" font-weight="700" font-size="74" fill="url(#titleFill)" textLength="430" lengthAdjust="spacingAndGlyphs">SUNRISE?</text>
    </svg>
    <p class="front-subtitle">How to Reverse the Clock and Feel Young Again</p>
    <div class="cover-photo" role="img" aria-label="Photo of a woman in her late forties looking frustrated, hand at her temple"></div>
    <div class="front-band">
      <p class="label bestseller">Best-Selling Author</p>
      <p class="author-name">ARLEN VOSS</p>
      <p class="author-role">Traditional Naturopath</p>
      <p class="foreword">foreword by Dr. Peter Lindqvist</p>
    </div>
  </section>

</div>
</body>
</html>
```